Email Banner (BrindleNotes)

We require an email banner for our email promotions sent to prospect clients. The banner needs to contain the wording BrindleNotes and use the same colour scheme as the logos attached.

This is for B2B professional's so needs to look like a place you would come to read technology articles.

```html
<!DOCTYPE html>
<html lang="en">
<head>
<meta charset="utf-8">
<title>BrindleNotes Email Banner</title>
<link rel="stylesheet" href="https://fonts.googleapis.com/css2?family=Lato:wght@400;700&family=Merriweather:wght@400&display=swap">
<style>
  :root {
    --page-bg: #f1f1f1;
    --banner-bg: #ffffff;
    --navy: #06131f;
    --ink: #3d3d3d;
    --photo-gray: #e6e6e6;
    --phone-blue: #1a8fd6;
    --web-teal: #2aa59e;
    --pin-green: #5bb56a;
    --bar-lime: #c4e3a4;
    --bar-mint: #a6dcbf;
    --bar-aqua: #92d2d3;
    --bar-sky: #66bbe4;
  }
  * { margin: 0; padding: 0; box-sizing: border-box; }
  html, body {
    width: 1200px;
    height: 960px;
    overflow: hidden;
    background: var(--page-bg);
  }
  .banner {
    position: absolute;
    left: 152px;
    top: 330px;
    width: 895px;
    height: 299px;
    background: var(--banner-bg);
    font-family: "Lato", sans-serif;
  }
  .banner-art {
    position: absolute;
    inset: 0;
  }
  .brand-name {
    position: absolute;
    left: 422px;
    top: 20px;
    font-size: 26px;
    font-weight: 700;
    color: var(--navy);
    letter-spacing: -0.2px;
  }
  .person-name {
    position: absolute;
    left: 380px;
    top: 98px;
    font-size: 24px;
    font-weight: 700;
    color: var(--navy);
    letter-spacing: 0.5px;
  }
  .person-role {
    position: absolute;
    left: 380px;
    top: 130px;
    font-family: "Merriweather", serif;
    font-size: 19px;
    color: var(--navy);
  }
  .role-rule {
    position: absolute;
    left: 380px;
    top: 162px;
    width: 128px;
    height: 2px;
    background: var(--navy);
  }
  .intro-text {
    position: absolute;
    left: 380px;
    top: 173px;
    width: 200px;
    font-size: 8.4px;
    line-height: 12px;
    color: var(--navy);
  }
  .contact-list {
    position: absolute;
    right: 111px;
    top: 88px;
    list-style: none;
    text-align: right;
    font-size: 15px;
    line-height: 18px;
    color: var(--ink);
  }
  .contact-list li { margin-bottom: 14px; }
</style>
</head>
<body>
  <section class="banner">
    <svg class="banner-art" width="895" height="299" viewBox="0 0 895 299" aria-hidden="true">
      <defs>
        <linearGradient id="fade-lime" x1="0" y1="0" x2="0" y2="1">
          <stop offset="0" stop-color="var(--bar-lime)"/><stop offset="1" stop-color="var(--bar-lime)" stop-opacity="0.85"/>
        </linearGradient>
        <linearGradient id="fade-mint" x1="0" y1="0" x2="0" y2="1">
          <stop offset="0" stop-color="var(--bar-mint)"/><stop offset="1" stop-color="var(--bar-mint)" stop-opacity="0.85"/>
        </linearGradient>
        <linearGradient id="fade-aqua" x1="0" y1="0" x2="0" y2="1">
          <stop offset="0" stop-color="var(--bar-aqua)"/><stop offset="1" stop-color="var(--bar-aqua)" stop-opacity="0.85"/>
        </linearGradient>
        <linearGradient id="fade-sky" x1="0" y1="0" x2="0" y2="1">
          <stop offset="0" stop-color="var(--bar-sky)"/><stop offset="1" stop-color="var(--bar-sky)" stop-opacity="0.85"/>
        </linearGradient>
      </defs>
      <polygon class="navy-slant" points="158,0 376,0 218,299 1,299" fill="var(--navy)"/>
      <circle class="photo-ring" cx="232" cy="150" r="102" fill="var(--banner-bg)"/>
      <circle cx="232" cy="150" r="97" fill="var(--navy)"/>
      <circle cx="232" cy="150" r="88" fill="var(--photo-gray)"/>
      <g class="growth-bars">
        <polygon points="523,265 564,240 564,299 523,299" fill="url(#fade-lime)"/>
        <polygon points="620,210 661,169 661,299 620,299" fill="url(#fade-mint)"/>
        <polygon points="719,120 760,100 760,299 719,299" fill="url(#fade-aqua)"/>
        <polygon points="816,66 857,28 857,299 816,299" fill="url(#fade-sky)"/>
      </g>
      <g class="contact-icons">
        <circle cx="815" cy="107" r="14" fill="var(--phone-blue)"/>
        <path d="M809.5,100.5 l3,0 1.2,3.5 -1.8,1.5 q1.5,3 4.6,4.6 l1.5,-1.8 3.5,1.2 0,3 q-1,1.5 -3,1.3 q-8,-1.5 -10.3,-10 q-0.2,-2 1.3,-3.3z" fill="#fff"/>
        <circle cx="815" cy="157" r="14" fill="var(--web-teal)"/>
        <g fill="none" stroke="#fff" stroke-width="1.3">
          <circle cx="815" cy="157" r="6.5"/>
          <ellipse cx="815" cy="157" rx="2.8" ry="6.5"/>
          <line x1="808.5" y1="157" x2="821.5" y2="157"/>
        </g>
        <circle cx="815" cy="206" r="14" fill="var(--pin-green)"/>
        <path d="M815,214 q-6,-7 -6,-10.5 a6,6 0 0 1 12,0 q0,3.5 -6,10.5z" fill="#fff"/>
        <circle cx="815" cy="203.5" r="2.2" fill="var(--pin-green)"/>
      </g>
    </svg>

    <div class="brand-name">BrindleNotes.io</div>

    <h1 class="person-name">NAME</h1>
    <p class="person-role">Your Position</p>
    <div class="role-rule"></div>
    <p class="intro-text">Lorem ipsum dolor sit amet, consectetuer adipiscings elit, sed diam nonummy nibh euismod tincidunts in ut laoreet dolore magna aliquam erat volutpat.</p>

    <ul class="contact-list">
      <li>123-456-7890<br>123-456-7890</li>
      <li>your mail Here<br>Your Website Here</li>
      <li>123 your address<br>State, City, 1234</li>
    </ul>
  </section>
</body>
</html>
```